Verpackungen für Trinkflasche
Zielgruppe
Wir produzieren Outdoor Artikel.
Aufgabenstellung
Es soll eine Verpackung für eine vakuumisolierte, doppelwandige Wasserflasche & Trinkflasche aus Hochwertigem Edelstahl designed werden. Die Flasche soll abgebildet sein, am besten halb offen (das Innere ist zu sehen) und halb geschlossen (das Äußere ist zu sehen). Die Besonderheiten und Eigenschaften sollen dann jeweils durch Pfeile möglichst modern /futuristisch kenntlich gemacht werden. Ich habe dafür Beispielbilder angehängt.
Die Besonderheiten:
Edelstahl
BPA-frei
doppelwandige Vakuumtechnologie
hält Getränke 24 h kalt
hält Getränke 12 h heiss
auslaufsicher
Flaschenhalterung inkl. Karabiner enthalten
500 mL
Titel auf der Verpackung in etwa so:
Trinkflasche
Outdoor / Sport / Abenteuer
Es muss Platz bleiben für einen ca. 4 x 2 cm großen Barcode (gibt es dann für den Gewinner zum Schluss des PRojektes zum Einfügen).
Die Trinkflasche wird es in 3 Farben geben: Blau, Schwarz, Grau
Zunächst bitte das Design für die blaue Flasche erstellen... das Gewinner-Design sollte dann noch auf die schwarze und graue angepasst werden.
Zusätzlich sollte jeweils ein 3D Mockup erstellt werden.
Zu den angehängten Bildern:
Es sind jeweils Beispielbilder der Farben gezeigt. Zusätzlich sind Design Beispiele gezeigt, wie ich mir ungefähr die Darstellung der Flaschen auf der Verpackung vorstelle.
Professionelle Fotos der Flaschen gibt es noch nicht. Hier bitte selbst aktiv werden oder bei z.B. Marktora umschauen (Beispiel: https://www.marktora.example/KELP-Flask-Vakuumisolierte-Doppelwandige-Isolierflasche/dp/Q07T3ZR4XD/ref=pd_cp_200_2?_encoding=UTF8&refRID=WQPLNHSAVD8EYTMBRXUC )
Der enthaltene Flaschenhalter ist ebenfalls gezeigt auf den Fotos, ich denke hier reicht eine schemenhafte Darstellung.
Fragen? Einfach stellen ;)

```html
<!DOCTYPE html>
<html lang="de">
<head>
<meta charset="utf-8">
<title>Thermo Trinkflasche – Verpackung Frontseite</title>
<link rel="stylesheet" href="https://fonts.googleapis.com/css2?family=Michroma&family=Jura:wght@500;700&display=swap">
<style>
  :root {
    --stage: #eeeeec;
    --panel-top: #ffffff;
    --panel-mid: #e4e6de;
    --panel-olive: #9ea66e;
    --panel-deep: #6c7a3a;
    --accent-green: #8bb733;
    --tagline-green: #7fae2a;
    --icon-grey: #8d918a;
    --icon-dark: #6e726b;
    --ink: #111111;
    --white: #ffffff;
    --bottle-blue-dark: #0d1f5c;
    --bottle-blue: #2a4fa8;
    --bottle-blue-light: #6f8fd6;
    --steel: #b9bdc0;
  }
  html, body {
    margin: 0;
    padding: 0;
    width: 1200px;
    height: 1200px;
    overflow: hidden;
    background: var(--stage);
  }
  .canvas {
    position: relative;
    width: 1200px;
    height: 1200px;
  }
  .pack-front {
    position: absolute;
    left: 410px;
    top: 40px;
    width: 380px;
    height: 1120px;
    background: linear-gradient(to bottom,
      var(--panel-top) 0%,
      var(--panel-mid) 35%,
      var(--panel-olive) 68%,
      var(--panel-deep) 100%);
    box-shadow: 0 0 0 1px #d6d8d0;
    overflow: hidden;
  }
  .brand {
    position: absolute;
    top: 38px;
    left: 0;
    right: 0;
    display: flex;
    justify-content: center;
    align-items: center;
    gap: 10px;
    font-family: "Jura", sans-serif;
    font-weight: 700;
    font-size: 30px;
    letter-spacing: 3px;
    color: var(--panel-deep);
  }
  .brand-dot {
    width: 16px;
    height: 16px;
    border-radius: 50%;
    background: var(--accent-green);
  }
  .tagline {
    position: absolute;
    top: 110px;
    left: 0;
    right: 0;
    text-align: center;
    font-family: "Jura", sans-serif;
    font-weight: 700;
    font-size: 19px;
    color: var(--tagline-green);
  }
  .bottle-visual {
    position: absolute;
    left: 128px;
    top: 160px;
    width: 230px;
    height: 600px;
    border-radius: 46% 46% 18px 18px / 30% 30% 18px 18px;
    background: linear-gradient(to right,
      var(--bottle-blue-dark) 0%,
      var(--bottle-blue) 30%,
      var(--bottle-blue-light) 45%,
      var(--bottle-blue-dark) 62%,
      #c7cacd 64%,
      var(--steel) 85%,
      #8f9498 100%);
  }
  .feature-icons {
    position: absolute;
    left: 28px;
    top: 170px;
    width: 76px;
  }
  .feature {
    position: absolute;
    left: 0;
    width: 76px;
    text-align: center;
  }
  .feature svg { display: block; }
  .feature-label {
    font-family: "Michroma", sans-serif;
    font-size: 17px;
    color: var(--ink);
    margin-top: 8px;
  }
  .detail {
    position: absolute;
    width: 84px;
    height: 84px;
    border-radius: 50%;
    border: 5px solid var(--accent-green);
    box-sizing: border-box;
  }
  .detail-base {
    left: 68px;
    top: 800px;
    background: radial-gradient(circle at 45% 45%, #f4f5f5, #9aa0a4 70%, #6d7276);
  }
  .detail-wall {
    left: 232px;
    top: 800px;
    background: linear-gradient(to right, #7a8086 0%, #d2d6d9 40%, #6e7379 55%, #bfe2f0 75%, #e9f6fb 100%);
  }
  .pointer-lines {
    position: absolute;
    left: 0;
    top: 0;
    width: 380px;
    height: 1120px;
    pointer-events: none;
  }
  .title {
    position: absolute;
    left: 0;
    right: 0;
    top: 905px;
    text-align: center;
    font-family: "Michroma", sans-serif;
    font-size: 50px;
    color: var(--ink);
    letter-spacing: 1px;
    line-height: 1;
  }
  .subtitle {
    position: absolute;
    left: 0;
    right: 0;
    top: 975px;
    text-align: center;
    font-family: "Michroma", sans-serif;
    font-size: 30px;
    color: var(--white);
    line-height: 1;
  }
  .volume {
    position: absolute;
    left: 0;
    right: 0;
    top: 1058px;
    text-align: center;
    font-family: "Michroma", sans-serif;
    font-size: 17px;
    color: var(--ink);
  }
</style>
</head>
<body>
<div class="canvas">
  <section class="pack-front">
    <div class="brand"><span class="brand-dot"></span>Trailkern</div>
    <div class="tagline">Outdoor / Sport / Abenteuer</div>

    <div class="bottle-visual" role="img" aria-label="Blaue Edelstahl-Thermoflasche mit silbernem Deckel, daneben angeschnittene Flasche mit sichtbarer Innenwand"></div>

    <div class="feature-icons">
      <div class="feature feature-leakproof" style="top:0">
        <svg width="76" height="76" viewBox="0 0 76 76" aria-label="auslaufsicher">
          <circle cx="38" cy="38" r="33" fill="var(--icon-grey)"/>
          <circle cx="38" cy="38" r="33" fill="none" stroke="var(--accent-green)" stroke-width="5"/>
          <path d="M32 26 C28 33 25 37 25 41 a7 7 0 0 0 14 0 c0-4-3-8-7-15z" fill="#3aa0e0"/>
          <path d="M46 34 C43 39 41 42 41 45 a5 5 0 0 0 10 0 c0-3-2-6-5-11z" fill="#3aa0e0"/>
          <line x1="16" y1="16" x2="60" y2="60" stroke="var(--accent-green)" stroke-width="5"/>
        </svg>
      </div>
      <div class="feature feature-cold" style="top:156px">
        <svg width="76" height="76" viewBox="0 0 76 76" aria-label="kalt">
          <circle cx="38" cy="38" r="33" fill="var(--icon-grey)"/>
          <path d="M38 5 A33 33 0 0 1 71 38" fill="none" stroke="var(--accent-green)" stroke-width="5"/>
          <path d="M5 38 A33 33 0 0 0 38 71" fill="none" stroke="var(--accent-green)" stroke-width="5"/>
          <g stroke="#2f9be6" stroke-width="3.5" stroke-linecap="round">
            <line x1="38" y1="22" x2="38" y2="54"/>
            <line x1="24" y1="30" x2="52" y2="46"/>
            <line x1="24" y1="46" x2="52" y2="30"/>
          </g>
        </svg>
        <div class="feature-label">24h</div>
      </div>
      <div class="feature feature-hot" style="top:330px">
        <svg width="76" height="76" viewBox="0 0 76 76" aria-label="heiß">
          <circle cx="38" cy="38" r="33" fill="var(--icon-grey)"/>
          <path d="M38 5 A33 33 0 0 1 71 38" fill="none" stroke="var(--accent-green)" stroke-width="5"/>
          <path d="M5 38 A33 33 0 0 0 38 71" fill="none" stroke="var(--accent-green)" stroke-width="5"/>
          <circle cx="38" cy="38" r="8" fill="#e8642a"/>
          <g stroke="#e8642a" stroke-width="3" stroke-linecap="round">
            <line x1="38" y1="20" x2="38" y2="26"/><line x1="38" y1="50" x2="38" y2="56"/>
            <line x1="20" y1="38" x2="26" y2="38"/><line x1="50" y1="38" x2="56" y2="38"/>
            <line x1="25" y1="25" x2="29" y2="29"/><line x1="47" y1="47" x2="51" y2="51"/>
            <line x1="25" y1="51" x2="29" y2="47"/><line x1="47" y1="29" x2="51" y2="25"/>
          </g>
        </svg>
        <div class="feature-label">12h</div>
      </div>
      <div class="feature feature-bpa" style="top:486px">
        <svg width="76" height="76" viewBox="0 0 76 76" aria-label="BPA-frei">
          <circle cx="38" cy="38" r="33" fill="var(--icon-grey)"/>
          <circle cx="38" cy="38" r="33" fill="none" stroke="var(--accent-green)" stroke-width="5"/>
          <text x="38" y="44" text-anchor="middle" font-family="Michroma, sans-serif" font-size="16" fill="var(--ink)">BPA</text>
          <line x1="16" y1="16" x2="60" y2="60" stroke="var(--accent-green)" stroke-width="5"/>
        </svg>
      </div>
    </div>

    <div class="detail detail-base" role="img" aria-label="Detail: Edelstahlboden der Flasche"></div>
    <div class="detail detail-wall" role="img" aria-label="Detail: doppelwandige Vakuumisolierung im Querschnitt"></div>

    <svg class="pointer-lines" viewBox="0 0 380 1120" aria-hidden="true">
      <g fill="none" stroke="var(--white)" stroke-width="2.5">
        <polyline points="152,842 170,842 170,788"/>
        <polyline points="274,800 274,786 320,786 320,765"/>
      </g>
      <g fill="var(--white)">
        <polygon points="164,790 176,790 170,776"/>
        <polygon points="314,767 326,767 320,753"/>
      </g>
    </svg>

    <div class="title">THERMO</div>
    <div class="subtitle">Trinkflasche</div>
    <div class="volume">500ML</div>
  </section>
</div>
</body>
</html>
```